Charity donation cards

I need a card in an envelope that would be given out to people and they would put their donations along with their details (name and email) and give it back to us (dropped in acrylic boxes at events etc).

The card should be a medium size, bi or tri fold to be able to fit all the information i require.

The Sarwa Fund

The Bright Meadow Centre is dedicated to providing the much needed support to families and children struggling with their differences through a holistic and comprehensive approach that includes detailed evaluations, therapy programs and support services to help unlock the potential in every child.

We are so proud to be able to help empower our society by dedicating our business to the mental, physical and social well being of our younger community and pledging all our net profits to help ensure no child is ever left behind.

Professional services can often be expensive. Our Sarwa Fund helps support families requiring financial aid. We believe every child deserves the opportunity to succeed and no child should be left behind.

How can you help?

Gift the therapies to the children that need it the most. We welcome new sponsors, appreciate your gifts and gratefully accept your contributions as we expand to increase the number of children we can serve.

Name:
Email:
Amount:

We accept cash, checks or credit card payments at The Bright Meadow Centre.

Gift cards should be dropped in the designated acrylic boxes at TBMC or the event.

Please email sarwafund@tbmc-example.ae for more information on the process.
Http://www.tbmc-example.ae

Target Market(s)

These cards will be placed in the reception for our clients to donate.

We will also be working with party planners. Some parents don't want people to get them gifts for their kids birthday party so they want to use this instead.

Industry/Entity Type

Charity

Requirements
Must have
• The same feel as our centre Http://www.tbmc-example.ae
• our website, email and contact number
Nice to have
• Go to our website and feel free to take ideas and content.
• The design should be clean and simple.
• High light the key words in the text with bold and maybe in green to make it pop out.
Should not have
• Do not use the word donate in any print material. The word should be gift.

```html
<!DOCTYPE html>
<html lang="en">
<head>
<meta charset="utf-8">
<title>The Sarwa Fund – Gift Card Layout</title>
<link rel="stylesheet" href="https://fonts.googleapis.com/css2?family=Arimo:wght@400;700&family=Raleway:wght@300&display=swap">
<style>
  :root{
    --ink:#555a5e;
    --ink-soft:#6b6f73;
    --label:#333;
    --green:#1d9a4a;
    --panel-edge:#e6e6e6;
    --frame:#444;
    --muted-square:#b9c3cc;
  }
  *{box-sizing:border-box;margin:0;padding:0}
  html,body{width:1200px;height:1000px;overflow:hidden;background:#fff}
  body{font-family:"Arimo",Arial,sans-serif;color:var(--ink)}
  .sheet{position:relative;width:1200px;height:1000px;border:2px solid var(--frame);background:#fff}
  .guide{position:absolute;color:var(--label);font-family:"Arimo",Arial,sans-serif}
  .guide--fold{top:41px;left:0;width:1200px;text-align:center;font-size:18px}
  .guide--back{top:428px;left:70px;font-size:34px}
  .guide--front{top:428px;left:1053px;font-size:34px}
  .guide--inside{top:938px;left:0;width:1206px;text-align:center;font-size:34px}

  .panel{position:absolute;width:390px;height:390px;border-radius:40px;
    background:radial-gradient(circle at 50% 45%,#fff 0%,#fbfbfb 55%,#ececec 100%)}
  .panel--back{left:210px;top:87px}
  .panel--front{left:601px;top:87px}
  .panel--about{left:210px;top:523px}
  .panel--help{left:601px;top:523px}

  .motif{position:absolute;border-radius:50%;
    background:radial-gradient(circle,rgba(120,190,160,.14) 0%,rgba(240,170,90,.08) 55%,rgba(255,255,255,0) 72%)}

  .contact-note{position:absolute;top:54px;left:0;width:390px;text-align:center;font-size:13.5px;line-height:18px;color:var(--ink-soft)}
  .contact-note strong{color:var(--ink)}

  .brand-mark{position:absolute;display:flex;align-items:center;gap:8px;font-family:"Raleway",Arial,sans-serif;font-weight:300;color:var(--ink-soft)}
  .brand-mark .dot{border-radius:50%;background:var(--green);flex:none}
  .brand-mark--small{left:38px;top:318px;font-size:13px;line-height:15px}
  .brand-mark--small .dot{width:14px;height:14px}
  .brand-mark--large{left:52px;top:100px;font-size:30px;line-height:34px}
  .brand-mark--large .dot{width:28px;height:28px}

  .social{position:absolute;left:286px;top:320px;width:70px;text-align:center;font-size:10.5px;color:var(--ink)}
  .social .squares{display:flex;justify-content:center;gap:3px;margin:2px 0 3px}
  .social .squares span{width:20px;height:20px;border-radius:4px;background:var(--muted-square)}

  .fund-title{position:absolute;left:0;top:276px;width:390px;text-align:center;font-weight:700;font-size:35px;color:var(--ink);letter-spacing:-.3px}
  .fund-tagline{position:absolute;left:137px;top:314px;font-family:"Raleway",Arial,sans-serif;font-weight:300;font-size:17px;color:var(--ink-soft)}

  .panel-heading{position:absolute;left:28px;top:45px;font-weight:700;font-size:20px;color:var(--ink)}
  .about-copy{position:absolute;left:30px;top:148px;width:318px;font-size:10.4px;line-height:12px;color:var(--ink)}
  .about-copy p{margin-bottom:12px}
  .hl{color:var(--green);font-weight:700}

  .help-copy{position:absolute;left:36px;top:149px;width:330px;font-size:12.6px;line-height:15.5px;color:var(--ink)}
  .gift-form{position:absolute;left:36px;top:217px;width:326px}
  .gift-form .row{display:flex;align-items:flex-end;height:23px;font-size:12.6px;color:var(--ink)}
  .gift-form .row span{width:56px;text-align:right;padding-right:6px}
  .gift-form .row i{flex:1;border-bottom:1px solid #bfbfbf;margin-bottom:3px}
  .payment-note{position:absolute;left:44px;top:294px;width:300px;font-size:10.2px;line-height:12.5px;color:var(--ink)}
</style>
</head>
<body>
<main class="sheet">
  <div class="guide guide--fold">fold here</div>
  <div class="guide guide--back">back</div>
  <div class="guide guide--front">front</div>
  <div class="guide guide--inside">inside</div>

  <section class="panel panel--back">
    <div class="motif" role="img" aria-label="decorative ring motif" style="left:-20px;top:60px;width:260px;height:200px"></div>
    <p class="contact-note">Please email us at<br><strong>sarwafund@tbmc-example.ae</strong><br>for more information on the process.</p>
    <div class="brand-mark brand-mark--small"><span class="dot"></span><span>The Bright Meadow<br>Centre</span></div>
    <div class="social">follow us :<div class="squares"><span></span><span></span><span></span></div>www.tbmc-example.ae</div>
  </section>

  <section class="panel panel--front">
    <div class="brand-mark brand-mark--large"><span class="dot"></span><span>The Bright<br>Meadow Centre</span></div>
    <h1 class="fund-title">The Sarwa Fund</h1>
    <p class="fund-tagline">open this flap to help ...</p>
  </section>

  <section class="panel panel--about">
    <div class="motif" role="img" aria-label="decorative ring motif" style="left:-20px;top:-10px;width:150px;height:140px"></div>
    <h2 class="panel-heading">The Sarwa Fund</h2>
    <div class="about-copy">
      <p>The Bright Meadow Centre is dedicated to providing the much needed support to families and children struggling with their differences through a holistic and comprehensive approach that includes detailed <span class="hl">evaluations, therapy programs and support services</span> to help unlock the potential in every child.</p>
      <p>We are so proud to be able to <span class="hl">help empower our society</span> by dedicating our business to the mental, physical and social well being of our younger community and pledging all our net profits to help ensure no child is ever left behind.</p>
      <p>Professional services can often be expensive. Our Sarwa Fund helps support families requiring <span class="hl">financial aid</span>. We believe every child deserves the opportunity to succeed and no child should be left behind.</p>
    </div>
  </section>

  <section class="panel panel--help">
    <div class="motif" role="img" aria-label="decorative ring motif" style="left:-20px;top:-10px;width:150px;height:140px"></div>
    <h2 class="panel-heading">How Can I Help ?</h2>
    <p class="help-copy"><span class="hl">Gift</span> the therapies to the children that need it the most. We welcome new sponsors, appreciate your gifts and gratefully accept your contributions as we expand to increase the number of children we can serve.</p>
    <div class="gift-form">
      <div class="row"><span>Name:</span><i></i></div>
      <div class="row"><span>Email:</span><i></i></div>
      <div class="row"><span>Amount:</span><i></i></div>
    </div>
    <p class="payment-note">We accept cash, checks or credit card payments at :<br>The Bright Meadow Centre.<br>Gift cards should be dropped in the designated<br>acrylic boxes at TBMC or the event.</p>
  </section>
</main>
</body>
</html>
```